RT Advisory - Web Design Upgrade

We have recently designed a website (http://www.rtadvisory-example.com.au) which requires more creative and professional inputs. The website was designed using 'bright hosting site builder template' and it is currently available for viewing on the internet. Also, you are able to access the PDF files for the 6 main pages (i.e. Home, About, Services, Contaminated Land Management, Groundwater Management and Contact).

The current website has 17 pages, however, your design may only be required for the 6 main pages.

Currently the website background is white but we are open to other colours provided the company logo is adjusted accordingly.

The idea is to upgrade the existing design and, if possible, continue using 'bright hosting' as the preferred web host. So we are not sure if the design should be coded or uncoded...we leave it to your proficiency and advice.

Target Market(s)

Government organisations, landowners and developers, waste and utilities companies, community organisations and individuals.

Font styles to use
Sans Serif

Colors
0355a3
3176b5
9ccb3b
acd037
ffffff

Requirements
Nice to have
• Sliding images

```html
<!DOCTYPE html>
<html lang="en">
<head>
<meta charset="utf-8">
<title>RT Advisory – Home</title>
<link href="https://fonts.googleapis.com/css2?family=Fira+Sans+Extra+Condensed:wght@500;600&family=PT+Sans:wght@400;700&family=Marck+Script&display=swap" rel="stylesheet">
<style>
:root{
  --page-green:#74b236;
  --brand-blue:#0457a0;
  --brand-blue-dark:#034a8a;
  --olive:#5e7131;
  --header-grey:#e2e2e2;
  --tab-active:#efefef;
  --nav-text:#555;
  --white:#fff;
}
*{margin:0;padding:0;box-sizing:border-box}
html,body{width:1200px;height:797px;overflow:hidden}
body{background:var(--page-green);font-family:"PT Sans",sans-serif;position:relative}
.page{position:absolute;left:131px;top:0;width:939px;height:797px;background:var(--header-grey);box-shadow:0 0 8px rgba(0,0,0,.35);overflow:hidden}
.topbar{position:absolute;left:0;top:0;width:100%;height:31px;background:var(--brand-blue)}
.search{position:absolute;left:749px;top:2px;width:179px;height:24px;border:1px solid #3176b5;background:#2a6db0;display:flex}
.search span{flex:1;color:#9fc0e3;font-style:italic;font-weight:700;font-size:12px;line-height:22px;padding-left:6px}
.search button{width:34px;border:0;background:#0b4a8c;display:flex;align-items:center;justify-content:center}
.brand{position:absolute;left:38px;top:62px;display:flex;align-items:center;gap:10px}
.brand .mark{width:34px;height:34px;border-radius:50%;background:var(--brand-blue)}
.brand .name{font-family:"Fira Sans Extra Condensed",sans-serif;font-weight:600;font-size:36px;color:var(--olive)}
.social{position:absolute;right:11px;top:44px;display:flex;gap:14px}
.social a{display:flex;align-items:center;gap:4px;color:var(--brand-blue);font-size:11px;text-decoration:none}
.social i{width:22px;height:22px;border-radius:50%;background:var(--brand-blue);display:block}
.tagline{position:absolute;left:502px;top:78px;width:432px;height:58px;border-top:1px dashed #777;border-bottom:1px dashed #777;text-align:right;white-space:nowrap;font-family:"Marck Script",cursive;font-size:27px;letter-spacing:-.3px;color:var(--olive);line-height:56px}
.nav{position:absolute;left:331px;top:147px;display:flex;height:56px}
.nav a{display:flex;align-items:center;justify-content:center;text-align:center;font-size:11.5px;color:var(--nav-text);text-decoration:none;border-left:1px solid #c8c8c8;line-height:1.25}
.nav a.active{background:var(--tab-active);color:var(--brand-blue);border-left:0}
.stripe{position:absolute;top:204px;left:0;width:100%;height:11px;background:var(--olive);border-bottom:1px solid #fff}
.stripe::before{content:"";position:absolute;left:0;top:0;width:236px;height:10px;background:var(--brand-blue)}
.hero{position:absolute;top:216px;left:0;width:100%;height:459px;background:linear-gradient(180deg,#3c62b8 0%,#6f92cf 45%,#8a9a6a 72%,#a08c52 100%)}
.arrow{position:absolute;top:198px}
.caption{position:absolute;top:675px;left:0;width:100%;height:80px;display:flex}
.caption .statement{width:633px;background:var(--brand-blue);color:var(--white);font-family:"Fira Sans Extra Condensed",sans-serif;font-weight:500;font-size:26px;line-height:33px;padding:7px 0 0 13px;white-space:nowrap;letter-spacing:-.3px}
.caption .service{flex:1;background:var(--olive);color:var(--white);font-family:"Fira Sans Extra Condensed",sans-serif;font-weight:600;font-size:31px;white-space:nowrap;display:flex;align-items:center;gap:6px;position:relative}
.caption .service svg{margin-left:-16px;flex:none}
.columns{position:absolute;top:787px;left:0;width:100%;height:10px}
.columns i{position:absolute;top:0;width:1px;height:10px;background:#bbb}
</style>
</head>
<body>
<div class="page">
  <div class="topbar">
    <div class="search"><span>Search...</span><button aria-label="Search">
      <svg width="18" height="16" viewBox="0 0 18 16"><circle cx="7" cy="6" r="4.5" fill="none" stroke="#fff" stroke-width="2"/><line x1="10.5" y1="9.5" x2="16" y2="14" stroke="#fff" stroke-width="2.5"/></svg>
    </button></div>
  </div>

  <div class="brand"><span class="mark"></span><span class="name">RT Advisory</span></div>

  <div class="social">
    <a href="#"><i></i>Chatter</a>
    <a href="#"><i></i>WorkNet</a>
    <a href="#"><i></i>Circles</a>
  </div>

  <div class="tagline">Working to Sustain our Environments</div>

  <nav class="nav">
    <a class="active" href="#" style="width:88px">HOME</a>
    <a href="#" style="width:102px">ABOUT</a>
    <a href="#" style="width:99px">SERVICES</a>
    <a href="#" style="width:126px">CONTAMINATED<br>LAND MANAGEMENT</a>
    <a href="#" style="width:111px">GROUNDWATER<br>MANAGEMENT</a>
    <a href="#" style="width:82px">Contact</a>
  </nav>

  <div class="stripe"></div>

  <div class="hero" role="img" aria-label="Slide photo: two consultants kneeling in a grassy field reviewing site plans under a blue sky">
    <svg class="arrow" style="left:15px" width="46" height="46" viewBox="0 0 46 46"><circle cx="23" cy="23" r="22" fill="rgba(255,255,255,.55)"/><path d="M33 23H14M21 15l-8 8 8 8" fill="none" stroke="#7f9ccc" stroke-width="5"/></svg>
    <svg class="arrow" style="left:878px" width="46" height="46" viewBox="0 0 46 46"><circle cx="23" cy="23" r="22" fill="rgba(255,255,255,.55)"/><path d="M13 23h19M25 15l8 8-8 8" fill="none" stroke="#7f9ccc" stroke-width="5"/></svg>
  </div>

  <div class="caption">
    <div class="statement">We are committed to delivering innovative and cost effective<br>solutions that can achieve sustainable and reliable outcomes</div>
    <div class="service">
      <svg width="28" height="20" viewBox="0 0 28 20"><path d="M26 10H4M11 3 4 10l7 7" fill="none" stroke="var(--olive)" stroke-width="3.5"/></svg>
      <span>PROJECT MANAGEMENT</span>
    </div>
  </div>

  <div class="columns"><i style="left:322px"></i><i style="left:649px"></i></div>
</div>
</body>
</html>
```